Successful Health Company Needs a Face Lift

We need a beautiful new design for our existing, online health supplements business.

Most of the elements are already there, but we need your sophistication and style.

The 3 pages that need your magic touch are:
Home page:
http://www.vitabrook.co.uk

Multiple Product pages. e.g:
http://www.vitabrook.co.uk/health-issues/major-organs/skin-hair-nails.html

Single Product pages. e.g:
http://www.vitabrook.co.uk/l-arginine-500-mg.html

Please have a look around.

This is a bilingual site, so all text (except logo) needs to be easily changed/translated. If photoshop files can be provided where we can simply translate the text layer of a graphic, that is acceptable. Please note that Greman words are generally longer than English.

Appearance:
The over all look should be open, light, uplifting and sophisticated.

The Home Page in detail:
We are largely happy with the category boxes in the centre column although you may restyle these if you wish.
The header, left menu and right column don't hang together and need your skills.

Logo:
We would like you to enhance our logo, but please note the 'S' and circle are used on many product labels, so we can't go too far from this just now.
(Product label example: http://www.vitabrook.co.uk/black-walnut-tincture-from-green-hull.html)

Header:
This needs to imply health and be light and stylish without it taking up valuable room.

Left Menu:
This is a multi-layer concertina menu. It is hard to see where your are within it. It needs to be made more clear and easy to navigate, maybe by using indentation and or better colour choices.
Please show it expanded and condensed in your design proposals.
(Extended menu example: http://www.vitabrook.co.uk/health-issues/female-health/thrush.html)

Multiple Product pages in detail
Please style the the brief descriptions, which must contain bullet points, price, add to basket and learn more.

Single Product pages in detail
The design and layout of this page needs to include all the elements currently there, including price, Qty, Add to Basket button, size and article number.

The static blocks on the right column will appear on these single product pages and need to suit the design well. They should not over-power the central content of the page.
Updates

Thank you all for participating.

Please note that what we are looking for is a more stylish and attractive version of what we already have.  The elements are all there.  We are not looking for a new concept.

We are happy for designers to switch images for better ones, work with colour ways, alter proportions and insert the elements in our brief.

We do not want to add banners, large images etc.  We want our customers to be familiar with what they see, and to be impressed with how much better the pages hang together.  They should not think they've landed at a new company.

We do want to see how the left menu looks when extended to show 2nd and 3rd tier menu titles.
We will also want to see how the design works for a multiple product page like this: http://www.vitabrook.co.uk/supplement-type/anti-microbials.html
as well as a single product page like this:  http://www.vitabrook.co.uk/black-walnut-extract.html

Some adjustment to the 'VitaBrook' logo is also an option and the graphic has been attached. 

Thank you for your careful attention to our brief.

Marcus.
pp Leopold

Project Deadline Extended
Reason: Due to unanticipated travel arrangements, the company director will only be available to make final decisions on Monday the 19th of March. Please continue updating submissions as we are in touch. Thank you for your understanding.

Target Market(s)

Health conscious women 70% men 30% aged 40 to 65 and health practitioners.

Industry/Entity Type

Health

Requirements
Must have
• Please include in the Header:
UK and German flags
Facebook, dig, +1, twitter, linked in, stumble upon
Padlock/SSL security/secure transaction
Practitioner helpline/ orders phone number
Paypal/Credit card logo

Please include in right column:
Clinician Corner
Mercury Free Dentistry
Shopping Basket
Storefronts for Therapists

Please include in either Header or Right Column
Same day dispatch
Money back warranty

```html
<!DOCTYPE html>
<html lang="en">
<head>
<meta charset="utf-8">
<title>VitaBrook – Home</title>
<link rel="stylesheet" href="https://fonts.googleapis.com/css2?family=Open+Sans:wght@400;600;700&display=swap">
<style>
:root{
  --pink:#d9477f;
  --pink-dark:#b8336a;
  --pink-soft:#e8709d;
  --aqua:#d5eef2;
  --aqua-line:#9fb9bd;
  --ink:#3d3d3d;
  --grey:#8a8a8a;
  --grey-band:#eeeeee;
  --white:#ffffff;
  --sky:#6cc6da;
}
*{box-sizing:border-box;margin:0;padding:0}
html,body{width:1200px;height:926px;overflow:hidden;background:var(--white)}
body{font-family:"Open Sans",Arial,sans-serif;color:var(--ink);position:relative}
.abs{position:absolute}

/* header */
.brand{left:140px;top:15px;height:62px;display:flex;align-items:center;gap:10px}
.brand-dot{width:60px;height:60px;border-radius:50%;border:4px solid var(--pink-soft)}
.brand-name{font-size:30px;font-weight:400;color:var(--sky);letter-spacing:.5px}
.account{right:145px;top:15px;font-size:12px;color:var(--grey)}
.perk{top:43px;height:33px;border:1px solid #dcdcdc;border-radius:6px;background:var(--white);
  display:flex;align-items:center;gap:9px;padding-left:9px;font-size:13px;color:var(--pink)}
.perk-icon{width:18px;height:18px;border-radius:3px;background:#8cc9e0}
.perk-icon.round{border-radius:50%;background:#c05a5a}
.helpline{left:864px;top:43px;width:194px;height:33px;border-radius:6px;
  background:linear-gradient(#e85b90,#c93371);color:var(--white);font-weight:700;font-size:12.5px;
  display:flex;align-items:center;gap:10px;padding-left:10px}
.helpline svg{flex:none}

.nav{left:380px;top:86px;width:680px;height:37px;border-top:1px solid #e2e2e2;display:flex;align-items:center}
.nav a{font-size:12px;color:#222;text-decoration:none;letter-spacing:.2px;padding:0 14px;line-height:37px}
.nav a.current{background:linear-gradient(#e3699a,#c73a74);color:var(--white);padding:0 16px}
.search{left:882px;top:95px;width:171px;height:21px;border:1px solid #cfcfcf;border-radius:3px;background:var(--white)}
.search svg{position:absolute;right:5px;top:4px}

/* left menu */
.az-head{left:140px;top:124px;width:221px;height:36px;background:var(--pink);
  font-size:16px;font-weight:700;color:#2c2c2c;padding:11px 0 0 22px}
.az-body{left:140px;top:160px;width:221px;height:411px;background:var(--aqua)}
.az-list{list-style:none;position:absolute;left:15px;width:193px}
.az-list li{height:28px;border-bottom:1px solid var(--aqua-line);font-size:13px;color:#333;
  padding:7px 0 0 7px;position:relative}
.az-list li.more::after{content:"+";position:absolute;right:6px;top:1px;font-size:20px;color:var(--white);font-weight:700}

.flyout{background:var(--aqua);border:1px solid #b6d6db;box-shadow:1px 1px 3px rgba(0,0,0,.15)}
.flyout div{height:28px;font-size:13px;color:#444;padding:5px 0 0 22px;border-bottom:1px solid #b9d3d7}
.flyout div.active{background:var(--pink);color:var(--white);position:relative}
.flyout div.active.arrow::after{content:"";position:absolute;right:9px;top:10px;border-left:5px solid var(--white);
  border-top:4px solid transparent;border-bottom:4px solid transparent}

/* centre */
.welcome{left:386px;top:166px;width:330px;text-align:right;font-size:34px;color:#b5306a}
.tile{width:220px;height:154px;border:1px solid #e6e6e6;overflow:hidden}
.tile-img{position:absolute;inset:0}
.tile-title{position:absolute;left:14px;top:12px;font-size:17px;font-weight:700;color:var(--pink-soft);letter-spacing:.3px}
.tile-cap{position:absolute;left:0;right:0;bottom:0;height:40px;background:rgba(255,255,255,.8);
  font-size:12px;line-height:15px;color:#3a3a3a;padding:6px 0 0 10px}
.tile-go{position:absolute;right:12px;bottom:10px;width:19px;height:19px;border-radius:50%;background:var(--pink)}
.tile-go svg{position:absolute;left:4px;top:4px}

/* right column */
.side{left:859px;width:201px;border:1px solid #c9e3e8;background:var(--white)}
.side-head{background:var(--aqua);font-size:11px;font-weight:600;color:#333;padding:6px 12px;letter-spacing:.2px;line-height:15px}
.side-img{position:absolute}
.side-text{position:absolute;font-size:10.5px;color:#333;letter-spacing:.3px;line-height:16px}
.pill{position:absolute;height:24px;border-radius:5px;background:linear-gradient(#ea6a9b,#c83a72);
  color:var(--white);font-size:11.5px;padding:4px 0 0;text-align:center}
.store-title{position:absolute;right:11px;top:12px;text-align:right;color:var(--pink);line-height:19px}
.phone{left:884px;top:672px;font-size:22px;font-weight:700;color:var(--pink)}
.payments{left:865px;top:708px;display:flex;gap:4px;align-items:center}
.card{width:31px;height:19px;border-radius:2px}

/* cart */
.cart{left:140px;top:593px;width:222px;height:131px;border:1px solid #cfcfcf}
.cart-head{height:28px;background:var(--pink);color:var(--white);font-size:12.5px;display:flex;align-items:center;gap:6px;padding-left:10px}
.cart-text{position:absolute;left:15px;top:54px;font-size:12.5px;line-height:19px;color:#333}

/* lower */
.social{left:143px;top:779px;display:flex;gap:7px}
.social span{width:22px;height:22px;border-radius:50%;background:#2f7fc1;display:block}
.pager{left:796px;top:772px;display:flex;gap:6px;font-size:13px;font-weight:700}
.pager span{width:22px;height:18px;text-align:center;line-height:18px}
.pager .on{background:#d3d3d3;color:#888}
.footer-links{left:140px;top:807px;width:920px;height:76px;background:var(--grey-band);
  font-size:10px;color:var(--grey);text-align:center;line-height:15px;padding:14px 40px 0}
.copyright{left:0;top:893px;width:1200px;text-align:center;font-size:10px;color:#555}
</style>
</head>
<body>

<header>
  <div class="abs brand"><span class="brand-dot"></span><span class="brand-name">VitaBrook</span></div>
  <div class="abs account">My basket | Login</div>
  <div class="abs perk" style="left:484px;width:179px"><span class="perk-icon"></span>Same day dispatch</div>
  <div class="abs perk" style="left:668px;width:186px"><span class="perk-icon round"></span>Money back warranty</div>
  <div class="abs helpline">
    <svg width="16" height="18" viewBox="0 0 16 18"><rect x="0" y="0" width="16" height="18" rx="3" fill="#fff"/><path d="M5 4c-1 1-1 3 1 6s4 4 5 3l-1.5-2-1.5.6c-1-.6-2-2-2.3-3.2l1.3-.8L6 4z" fill="#c93371"/></svg>
    PRACTITIONER HELPLINE
  </div>
  <nav class="abs nav">
    <a class="current">HOME</a><a>DETOX</a><a>HYDRATION</a><a>SUPPLEMENTS</a><a>YOUR HEALTH ISSUES</a>
  </nav>
  <div class="abs search">
    <svg width="11" height="11" viewBox="0 0 11 11"><circle cx="4.5" cy="4.5" r="3.3" fill="none" stroke="#d9477f" stroke-width="1.5"/><path d="M7 7l3 3" stroke="#d9477f" stroke-width="1.5"/></svg>
  </div>
</header>

<aside>
  <div class="abs az-head">A to Z</div>
  <div class="abs az-body">
    <ul class="az-list" style="top:10px">
      <li class="more">Supplement Type</li><li class="more">Your Health Issue</li><li class="more">Expert Product Lines</li>
    </ul>
    <ul class="az-list" style="top:108px">
      <li class="more">Detox &amp; Cleansing</li><li class="more">Hydration &amp; Water</li><li class="more">Natural Body Care</li>
    </ul>
    <ul class="az-list" style="top:206px">
      <li>Sport &amp; Fitness</li><li>Health Technology</li><li>Household Products</li>
    </ul>
    <ul class="az-list" style="top:305px">
      <li>Laboratory Tests</li><li>Books &amp; Education</li><li>New &amp; Special Offers</li>
    </ul>
  </div>
</aside>

<main>
  <h1 class="abs welcome" style="font-weight:400">Welcome to VitaBrook</h1>

  <div class="abs tile" style="left:380px;top:253px">
    <div class="tile-img" role="img" aria-label="Photo of a woman holding her stomach" style="background:linear-gradient(120deg,#fafafa 30%,#f0d9cf)"></div>
    <div class="tile-title">DIGESTION</div>
    <div class="tile-cap">Constipation, Candida<br>Irritable Bowel, Wind</div>
    <div class="tile-go"><svg width="11" height="11" viewBox="0 0 11 11"><path d="M1 5.5h8M6 2l3.5 3.5L6 9" stroke="#fff" stroke-width="2" fill="none"/></svg></div>
  </div>
  <div class="abs tile" style="left:623px;top:253px">
    <div class="tile-img" role="img" aria-label="Photo of a man holding his aching shoulder" style="background:linear-gradient(90deg,#fafafa 35%,#8a5a3e 70%,#f5f5f5)"></div>
    <div class="tile-title">PAIN</div>
    <div class="tile-cap">Back Pain, Joint and Bone<br>Headaches, Period Pain</div>
    <div class="tile-go"><svg width="11" height="11" viewBox="0 0 11 11"><path d="M1 5.5h8M6 2l3.5 3.5L6 9" stroke="#fff" stroke-width="2" fill="none"/></svg></div>
  </div>
  <div class="abs tile" style="left:380px;top:427px">
    <div class="tile-img" role="img" aria-label="Photo of a slim waist in loose jeans" style="background:linear-gradient(90deg,#f4f4f4,#e6d6cc 40%,#f7f7f7 70%)"></div>
    <div class="tile-title">WEIGHT LOSS</div>
    <div class="tile-cap">Constipation, Candida<br>Irritable Bowel, Wind</div>
    <div class="tile-go"><svg width="11" height="11" viewBox="0 0 11 11"><path d="M1 5.5h8M6 2l3.5 3.5L6 9" stroke="#fff" stroke-width="2" fill="none"/></svg></div>
  </div>
  <div class="abs tile" style="left:623px;top:427px">
    <div class="tile-img" role="img" aria-label="Photo of a back massage" style="background:linear-gradient(160deg,#5a3426,#d9a489 50%,#e9c6b3)"></div>
    <div class="tile-title">BODY CARE</div>
    <div class="tile-cap">Back Pain, Joint and Bone<br>Headaches, Period Pain</div>
    <div class="tile-go"><svg width="11" height="11" viewBox="0 0 11 11"><path d="M1 5.5h8M6 2l3.5 3.5L6 9" stroke="#fff" stroke-width="2" fill="none"/></svg></div>
  </div>
  <div class="abs tile" style="left:380px;top:601px">
    <div class="tile-img" role="img" aria-label="Illustration of the brain on a head" style="background:linear-gradient(180deg,#f7f7f7,#d9b8a5 45%,#c9a08a)"></div>
    <div class="tile-title">BRAIN HEALTH</div>
    <div class="tile-cap">Constipation, Candida<br>Irritable Bowel, Wind</div>
    <div class="tile-go"><svg width="11" height="11" viewBox="0 0 11 11"><path d="M1 5.5h8M6 2l3.5 3.5L6 9" stroke="#fff" stroke-width="2" fill="none"/></svg></div>
  </div>
  <div class="abs tile" style="left:623px;top:601px">
    <div class="tile-img" role="img" aria-label="Photo of a woman drinking a glass of water" style="background:linear-gradient(90deg,#fafafa 50%,#e9cfc0 75%,#5b3a2c)"></div>
    <div class="tile-title">WATER &amp; HYDRATION</div>
    <div class="tile-cap">Back Pain, Joint and Bone<br>Headaches, Period Pain</div>
    <div class="tile-go"><svg width="11" height="11" viewBox="0 0 11 11"><path d="M1 5.5h8M6 2l3.5 3.5L6 9" stroke="#fff" stroke-width="2" fill="none"/></svg></div>
  </div>

  <div class="abs pager"><span class="on">1</span><span>2</span></div>
</main>

<!-- submenu flyouts sit above the heading -->
<div class="abs flyout" style="left:362px;top:160px;width:117px;height:183px;padding-top:7px">
  <div class="active arrow">Input link</div><div>Input Link</div><div>Input link</div><div>Input link</div><div>Input Link</div><div>Input link</div>
</div>
<div class="abs flyout" style="left:479px;top:160px;width:116px;height:77px;padding-top:7px">
  <div class="active">Input link</div><div>Input Link</div>
</div>

<aside>
  <section class="abs side" style="top:253px;height:131px">
    <div class="side-head">CLINICIAN CORNER</div>
    <div class="side-img" role="img" aria-label="Photo of a practitioner in a white coat" style="left:4px;top:30px;width:62px;height:98px;background:linear-gradient(#e5eef2,#c9d6dd)"></div>
    <div class="side-text" style="left:72px;top:48px">CONTACT A NATURAL<br>HEALTH PRACTITIONER</div>
    <div class="pill" style="left:104px;top:97px;width:87px">Contact Now</div>
  </section>
  <section class="abs side" style="top:401px;height:131px">
    <div class="side-head">MERCURY FREE DENTIST<br>UK &amp; IRELAND</div>
    <div class="side-img" role="img" aria-label="Photo of a smiling woman" style="left:0;top:38px;width:130px;height:92px;background:linear-gradient(90deg,#e9d3a0,#f3e2cf 60%,#fff)"></div>
    <div class="side-text" style="left:96px;top:62px;width:100px;text-align:center;font-weight:600;line-height:13px">A<br>COMPREHENSIVE<br>LIST</div>
    <div class="pill" style="left:104px;top:102px;width:87px">Available here</div>
  </section>
  <section class="abs side" style="top:548px;height:111px;border-color:#cfcfcf">
    <div class="side-img" role="img" aria-label="Illustration of boxes on a hand truck" style="left:8px;top:22px;width:80px;height:80px;background:radial-gradient(circle,#d8c4a4,#fff 70%)"></div>
    <div class="store-title"><span style="font-size:17px;font-weight:600">Storefronts</span><br><span style="font-size:14px">for</span><br><span style="font-size:13px">Therapists</span></div>
    <svg class="side-img" style="left:167px;top:80px" width="20" height="20" viewBox="0 0 20 20"><circle cx="10" cy="10" r="9" fill="#e4eef2" stroke="#b8c9cf"/><path d="M5 10h9M11 6l4 4-4 4" stroke="#a9b9bf" stroke-width="1.6" fill="none"/></svg>
  </section>
  <div class="abs phone">01632 960 418</div>
  <div class="abs payments">
    <svg width="20" height="24" viewBox="0 0 20 24"><path d="M5 11V7a5 5 0 0110 0v4" stroke="#8f8f8f" stroke-width="2.4" fill="none"/><rect x="1" y="10" width="18" height="14" rx="2" fill="#e1b52e"/></svg>
    <span class="card" style="background:#d23b2f"></span><span class="card" style="background:#1a3f8f"></span><span class="card" style="background:#3a8fc9"></span><span class="card" style="background:#2d5ea8"></span><span class="card" style="background:#f2f2f2;border:1px solid #ddd"></span>
  </div>

  <section class="abs cart">
    <div class="cart-head">
      <svg width="20" height="14" viewBox="0 0 20 14"><path d="M0 1h4l3 8h10l2-6H6" stroke="#fff" stroke-width="1.8" fill="none"/><circle cx="8" cy="12.5" r="1.4" fill="#fff"/><circle cx="16" cy="12.5" r="1.4" fill="#fff"/></svg>
      SHOPPING CART
    </div>
    <p class="cart-text">You have<br>no items in your<br>shopping basket.</p>
    <div class="side-img" role="img" aria-label="Illustration of a red shopping trolley" style="left:146px;top:36px;width:68px;height:90px;background:radial-gradient(circle,#e57068,#fff 72%)"></div>
  </section>
</aside>

<footer>
  <div class="abs social"><span style="background:#3aa7d9"></span><span style="background:#2a6aa6"></span><span style="background:#2f5a8f"></span><span style="background:#3a66b0"></span><span style="background:#4d8f3a"></span><span style="background:#8a8a8a"></span></div>
  <div class="abs footer-links">Kidney Pain | Kidney Stones | Kidney Disease Symptoms | Colon Cleanse | Digestive Enzymes | Digestive Enzymes Supplement | Healing Principles | Herbal Remedies | Herbal Remedies for Anxiety | Herbal Remedies for Constipation | Herbal Remedies for Depression | Herbal Remedies for Menopause Bloated Stomach | Health Shops Norvale<br>What is Mercury Free Dentistry?</div>
  <div class="abs copyright">© 2010 VitaBrook Enterprises. All Rights Reserved.</div>
</footer>

</body>
</html>
```